Herbalist's Pain Cream WIX Website Redesign

I need a complete WIX website redesign! I am an herbalist and I'm relaunching my company, starting with a pain cream as the flagship product. My natural pain relief cream is composed of 6 active botanicals, uses all natural preservatives and provides pain relief within 1 minute! I have a new label design that reflects the high quality of this product and its ingredients. I have the content written and a rough website outline. I want the new website to match the color scheme of the label, and to show the quality of the product. (Logo uploaded is older color scheme. See New Label upload for updated color scheme.) I will be launching more products in the future, but the current content is for 1 flagship product. I want a high quality, earthy/ natural, botanical medicine feel. SEO phrase "Natural Pain Relief Cream" Old website is up again, for pictures: www.tolvenleaf.com

Target Market(s)

Middle to later aged women, Same for Men, but usually introduced by woman in their life

Industry/Entity Type

Botanical Supplement

Coding

Coded - Design and coding required

Number of Pages Required

5+ page

Colors
0054AA
0677BA
7BADD7
CADEEF
E8F1F8

Requirements
Must have
• Homepage, About, Ingredients, Shop, Contact Us
Nice to have
• FAQ section, maybe graphics to highlight unique elements

```html
<!DOCTYPE html>
<html lang="en">
<head>
<meta charset="utf-8">
<title>Tolvenleaf Herbal Remedies</title>
<link rel="stylesheet" href="https://fonts.googleapis.com/css2?family=DM+Sans:wght@400;500;600;700&family=Noto+Serif:wght@400;500&family=Open+Sans:wght@400;600&display=swap">
<style>
:root{
  --blue:#0054AA;
  --blue-mid:#0677BA;
  --blue-soft:#7BADD7;
  --blue-pale:#CADEEF;
  --blue-mist:#E8F1F8;
  --navy:#0d3b66;
  --teal:#3a9fa5;
  --mint:#eef7f6;
  --grey-bg:#f8f8f8;
  --ink:#1c1c1c;
  --muted:#555;
  --line:#dcdcdc;
}
*{box-sizing:border-box;margin:0;padding:0}
html,body{width:1200px;height:4041px;overflow:hidden}
body{position:relative;background:#fff;font-family:"DM Sans",sans-serif;color:var(--ink)}
.abs{position:absolute}
.btn{position:absolute;background:var(--blue);color:#fff;font:600 15px "DM Sans",sans-serif;border-radius:4px;display:flex;align-items:center;justify-content:center;text-decoration:none}
.photo{position:absolute}

/* header */
.site-header{position:absolute;left:0;top:0;width:1200px;height:97px;background:#fff}
.brand{position:absolute;display:flex;align-items:center;gap:10px;color:var(--teal);font-family:"DM Sans",sans-serif;font-weight:400;line-height:1}
.brand .dot{border-radius:50%;background:var(--teal)}
.brand .name{display:flex;flex-direction:column}
.brand.top{left:86px;top:22px}
.brand.top .dot{width:46px;height:46px}
.brand.top .name span:first-child{font-size:27px}
.brand.top .name span:last-child{font-size:12px;letter-spacing:1px;margin-top:3px}
.nav a{position:absolute;top:40px;font-size:15px;color:#333;text-decoration:none}
.nav a.active{color:var(--blue);font-weight:600}

/* hero */
.hero{position:absolute;left:0;top:97px;width:1200px;height:560px;background:var(--mint)}
.hero h1{position:absolute;left:86px;top:118px;width:680px;font:400 34px/46px "Noto Serif",serif;color:var(--navy)}

/* features */
.feature{position:absolute;top:711px;width:311px;height:144px;border:1px solid #e3e3e3;background:#fff;text-align:center}
.feature .num{position:absolute;left:50%;top:-20px;transform:translateX(-50%);width:40px;height:40px;border-radius:50%;background:var(--navy);color:#fff;font:400 24px/40px "Noto Serif",serif}
.feature h3{margin-top:30px;font:500 13px/20px "DM Sans",sans-serif;color:#5a7a9a;padding:0 90px}
.feature p{margin-top:14px;font-size:11.5px;line-height:17px;color:#555;padding:0 30px}

/* relief */
.relief{position:absolute;left:0;top:907px;width:1200px;height:436px;background:var(--grey-bg)}
.relief h2{position:absolute;left:86px;top:89px;width:460px;font:500 32px/41px "DM Sans",sans-serif;color:#111}
.relief p{position:absolute;left:86px;top:180px;width:390px;font-size:13px;line-height:20px;color:#333}
.relief .tag{position:absolute;left:94px;top:256px;font-size:15px;font-weight:500;color:#111}

/* ingredients */
.ingr .kicker{position:absolute;left:571px;top:1376px;font-size:19px;color:#222}
.ingr h2{position:absolute;left:571px;top:1405px;width:560px;font:500 36px/41px "DM Sans",sans-serif;color:#222}
.ingr h2 strong{font-weight:600;color:var(--navy)}
.ingr p{position:absolute;left:571px;width:555px;font-size:13px;line-height:25px;color:#333}

/* expert */
.expert h2{position:absolute;left:86px;top:2063px;width:560px;font:500 32px/42px "DM Sans",sans-serif;color:#111}
.expert p{position:absolute;left:86px;top:2163px;width:520px;font-size:12.5px;line-height:20px;color:#333}

/* testimonials */
.testi .label{position:absolute;left:0;width:1200px;top:2516px;text-align:center;font-size:19px;color:#222}
.testi h3{position:absolute;left:0;width:1200px;top:2580px;text-align:center;font:500 29px "DM Sans",sans-serif;color:#111}
.testi p{position:absolute;left:295px;width:610px;top:2626px;text-align:center;font-size:10.5px;line-height:13px;color:#444}
.testi .stars{position:absolute;left:0;width:1200px;top:2677px;text-align:center;color:var(--blue-soft);font-size:20px;letter-spacing:4px}
.testi .rule{position:absolute;left:505px;top:2710px;width:190px;height:1px;background:#ccc}
.testi .who{position:absolute;left:0;width:1200px;top:2729px;text-align:center;font-size:14px;color:#555}
.quote{position:absolute;top:2577px;font:700 34px/1 "Noto Serif",serif;color:#111}

/* faq */
.faq{position:absolute;left:0;top:2777px;width:1200px;height:627px;background:var(--blue)}
.faq-item{position:absolute;left:97px;width:582px;border:1px solid rgba(255,255,255,.18);color:#fff}
.faq-item .q{position:absolute;left:26px;top:26px;font-size:13px;font-weight:600;line-height:16px}
.faq-item .q:before{content:"\2726";margin-right:12px}
.faq-item .icon{position:absolute;right:18px;top:21px;font-size:22px;font-weight:300;line-height:22px}
.faq-item.open{border-color:rgba(255,255,255,.6)}
.faq-item.open .icon{font-size:15px;top:26px}
.faq-item.open p{position:absolute;left:20px;top:66px;width:540px;font-size:10.5px;line-height:17px;color:#c8d9ee}
.faq-side .rule{position:absolute;left:990px;top:3050px;width:56px;height:2px;background:#fff}
.faq-side .tag{position:absolute;right:97px;top:3038px;font-size:19px;line-height:24px;color:var(--blue-soft)}
.faq-side h2{position:absolute;right:97px;top:3070px;font:500 29px/38px "DM Sans",sans-serif;color:#fff;white-space:nowrap}
.faq-side p{position:absolute;right:97px;top:3128px;font-size:11.5px;line-height:16px;color:var(--blue-pale);white-space:nowrap}

/* cta */
.cta h2{position:absolute;left:0;width:1200px;top:3474px;text-align:center;font:600 35px "Open Sans",sans-serif;color:#555}
.cta .sub{position:absolute;left:0;width:1200px;top:3535px;text-align:center;font-size:13px;color:#444}
.cta .field{position:absolute;left:366px;top:3589px;width:337px;height:53px;background:#eee;border-radius:4px 0 0 4px;font-size:12px;color:#aaa;padding:20px 16px}

/* footer */
.site-footer{position:absolute;left:0;top:3682px;width:1200px;height:359px;background:var(--grey-bg)}
.brand.foot{left:97px;top:3728px}
.brand.foot .dot{width:60px;height:60px}
.brand.foot .name span:first-child{font-size:38px}
.brand.foot .name span:last-child{font-size:17px;letter-spacing:1px;margin-top:4px}
.news-label{position:absolute;left:97px;top:3843px;font-size:13px;color:#aaa}
.news-field{position:absolute;left:113px;top:3880px;font-size:12px;color:#666}
.col h4{position:absolute;top:3708px;font-size:15px;font-weight:600;color:#111}
.col a{position:absolute;font-size:13px;color:#666;text-decoration:none}
.foot-rule{position:absolute;left:97px;top:3973px;width:1006px;height:1px;background:#ccc}
.copy{position:absolute;left:0;width:1200px;top:4004px;text-align:center;font-size:11px;color:#444}
</style>
</head>
<body>

<header class="site-header">
  <div class="brand top"><span class="dot"></span><span class="name"><span>TOLVENLEAF</span><span>HERBAL REMEDIES</span></span></div>
  <nav class="nav">
    <a class="active" style="left:704px">Home</a>
    <a style="left:769px">Ingridients</a>
    <a style="left:864px">About</a>
    <a style="left:929px">Shop</a>
    <a style="left:987px">FAQ</a>
    <a style="left:1037px">Contact us</a>
  </nav>
</header>

<section class="hero">
  <h1>Welcome to Tolvenleaf Herbal Remedies, where the wisdom of nature meets the art of healing.</h1>
</section>
<svg class="abs" style="left:0;top:500px" width="1200" height="160" viewBox="0 0 1200 160">
  <path d="M0 110 C250 20 450 40 700 95 C900 140 1050 120 1200 80 L1200 160 L0 160Z" fill="#fff"/>
  <path d="M240 20 C500 10 700 90 930 130" stroke="#dceeed" stroke-width="6" fill="none"/>
</svg>
<div class="photo" role="img" aria-label="Bowls of herbal powder, cream and honey with green leaves on burlap" style="left:860px;top:110px;width:340px;height:533px;border-radius:0 0 0 120px;background:radial-gradient(circle at 55% 45%,#f3efe6 0%,#c9b48f 55%,#a48660 100%)"></div>
<a class="btn" style="left:86px;top:392px;width:168px;height:60px">Explore product</a>

<div class="feature" style="left:97px"><span class="num">1</span><h3>Expertly Crafted Formula</h3><p>Formulated by an herbalist with over a decade of clinical experience.</p></div>
<div class="feature" style="left:444px"><span class="num">2</span><h3 style="padding:0 80px">Fast-Acting Ingredients</h3><p>With nature's power at the forefront, our 6 active botanicals deliver almost instant relief</p></div>
<div class="feature" style="left:791px"><span class="num">3</span><h3 style="padding:0 40px;margin-top:33px">Nurturing Touch</h3><p style="margin-top:20px">Not only does our natural pain relief cream alleviate discomfort, but it also nourishes and rejuvenates your skin.</p></div>

<section class="relief">
  <h2>Feel the Difference in Just 1 Minute!</h2>
  <p>Whether you're overcoming the strains of daily life or the demands of an active lifestyle, our natural pain relief cream is your go-to solution for quick relief.</p>
  <div class="tag">Apply, Relax, and Reclaim Your Day—Experience Relief Today!</div>
</section>
<a class="btn" style="left:86px;top:1200px;width:168px;height:58px">Buy now</a>
<div class="photo" role="img" aria-label="Jar of pain cream with a pale blue botanical label" style="left:827px;top:1009px;width:263px;height:249px;border-radius:14px;background:linear-gradient(180deg,#f4f4f4 0%,#e6e6e6 28%,#c9dcef 30%,#b7cde6 100%)"></div>

<section class="ingr">
  <div class="photo" role="img" aria-label="White yarrow flowers" style="left:0;top:1343px;width:318px;height:279px;background:linear-gradient(135deg,#556b3c,#e9ece3 50%,#6d7f4a)"></div>
  <div class="photo" role="img" aria-label="Open jar of white cream seen from above" style="left:0;top:1622px;width:318px;height:238px;background:radial-gradient(circle at 40% 55%,#e8f2fa,#a9c4dc 70%,#7a8ea2)"></div>
  <div class="photo" role="img" aria-label="Glass dropper over a small vial of extract" style="left:318px;top:1343px;width:200px;height:517px;background:linear-gradient(180deg,#efe4cf,#dccba9 60%,#cdb88f)"></div>
  <div class="kicker">Ingridients</div>
  <h2><strong>We use herbs harvested from themwild and from the farm</strong>, to deliver a potent natural healing experience.</h2>
  <p style="top:1581px">At Tolvenleaf Herbal Remedies, we understand that when discomfort strikes, you seek swift and effective relief. That's why it is important to use the most powerful botanical ingredients in our natural pain relief cream. Each ingredient reflects acommitment to quality and efficacy, harnessing the powerful properties of nature's finest ingredients.</p>
  <p style="top:1706px">Try our <strong>natural pain relief cream</strong> and let the calming embrace of nature guide you toward a place of comfort and vitality.</p>
  <a class="btn" style="left:571px;top:1777px;width:204px;height:58px">Explore the ingridients</a>
</section>

<section class="expert">
  <svg class="abs" style="left:0;top:1860px" width="1200" height="600" viewBox="0 0 1200 600">
    <path d="M0 95 C300 40 600 120 900 110 C1050 105 1150 60 1200 20 L1200 580 C1000 560 800 580 600 575 C350 570 150 570 0 575Z" fill="var(--mint)"/>
    <path d="M0 95 C250 50 500 80 760 135" stroke="#e3f1ef" stroke-width="8" fill="none"/>
  </svg>
  <div class="photo" role="img" aria-label="Portrait of the founder outdoors in the mountains" style="left:828px;top:1976px;width:372px;height:479px;border-radius:40px 0 0 0;background:linear-gradient(160deg,#9fb0bd 0%,#b79a80 45%,#8b6f57 100%)"></div>
  <h2>Experience the Difference That Expertise Makes!</h2>
  <p>Meet Elias, the creator of Tolvenleaf Herbal Remedies. Inspired by his personal journey to heal his chronic pain, he devoted his life to studying medicinal plants and how to harness their healing abilities to improve the lives of others. As a trained herbalist, botanical medicine researcher and supplement formulator, let Elias's expertise guide you back to health and wellness. Discover the restorative power of herb-based solutions at Tolvenleaf Herbal Remedies!</p>
  <a class="btn" style="left:86px;top:2301px;width:168px;height:58px">Read more</a>
</section>

<section class="testi">
  <div class="label">Testimonials</div>
  <span class="quote" style="left:157px">&ldquo;</span>
  <span class="quote" style="left:1019px">&rdquo;</span>
  <h3>Better than prescription pain meds</h3>
  <p>Tolvenleaf Herbal Remedies pain cream is by far 10000000xbetter than any prescription pain medication that I've ever taken. So please, if you suffer from occasional neuropathies ,muscle pain, back pain, elbow, shoulder... pretty much anything related along those lines – BUY THIS ASAP!!!! You'll thank me.</p>
  <div class="stars">★★★★★</div>
  <div class="rule"></div>
  <div class="who">Maren T. Sarasota, FL</div>
  <svg class="abs" style="left:50px;top:2636px" width="16" height="30"><path d="M14 2 L2 15 L14 28" stroke="#777" stroke-width="2" fill="none"/></svg>
  <svg class="abs" style="left:1122px;top:2636px" width="16" height="30"><path d="M2 2 L14 15 L2 28" stroke="#7BADD7" stroke-width="2" fill="none"/></svg>
</section>

<section class="faq"></section>
<div class="faq-item open" style="top:2805px;height:165px"><span class="q">Does it work?</span><span class="icon">✕</span><p>Absolutely! You will start to feel relief within 1 minute. After 15 minutes you will feel its full effects. At Tolvenleaf Herbal Remedies, we stand by the effectiveness of our Pain Cream, which is truly more than just a product—it's a carefully crafted solution born from clinical experience and expertise.</p></div>
<div class="faq-item" style="top:2990px;height:70px"><span class="q">Who is this natural pain relief cream for?</span><span class="icon">+</span></div>
<div class="faq-item" style="top:3067px;height:70px"><span class="q">How do I use it?</span><span class="icon">+</span></div>
<div class="faq-item" style="top:3145px;height:70px"><span class="q">How long is your pain cream good for?</span><span class="icon">+</span></div>
<div class="faq-item" style="top:3222px;height:70px"><span class="q">Are your preservatives natural?</span><span class="icon">+</span></div>
<div class="faq-item" style="top:3299px;height:70px"><span class="q">What's your shipping and delivery times?</span><span class="icon">+</span></div>
<div class="faq-side">
  <div class="rule"></div>
  <div class="tag">FAQ</div>
  <h2>Ask us anything</h2>
  <p>Have any questions? We're here to assist you.</p>
</div>

<section class="cta">
  <div class="photo" role="img" aria-label="Decorative flowing blue line pattern" style="left:0;top:3404px;width:120px;height:278px;background:linear-gradient(90deg,rgba(6,119,186,.25),rgba(6,119,186,0))"></div>
  <div class="photo" role="img" aria-label="Decorative flowing blue line pattern" style="left:1020px;top:3450px;width:180px;height:232px;border-radius:120px 0 0 0;background:linear-gradient(270deg,rgba(6,119,186,.25),rgba(6,119,186,0))"></div>
  <h2>Start Your Journey With Us</h2>
  <div class="sub">Where The Wisdom Of Nature Meets The Art Of Healing.</div>
  <div class="field">Your Emai</div>
  <a class="btn" style="left:703px;top:3589px;width:130px;height:53px;font-size:13px">Contact Us</a>
</section>

<footer class="site-footer"></footer>
<div class="brand foot"><span class="dot"></span><span class="name"><span>TOLVENLEAF</span><span>HERBAL REMEDIES</span></span></div>
<div class="news-label">Get Our Weekly Newsletter (Zero Spam)</div>
<div class="news-field">Type In Your Email</div>
<a class="btn" style="left:314px;top:3868px;width:70px;height:40px;font-size:13px">Send</a>
<div class="col">
  <h4 style="left:695px">Navigation</h4>
  <a style="left:695px;top:3742px">Home</a>
  <a style="left:695px;top:3776px">About</a>
  <a style="left:695px;top:3810px">Ingridients</a>
  <a style="left:695px;top:3844px">Shop</a>
  <a style="left:695px;top:3878px">FAQ</a>
  <a style="left:695px;top:3912px">Contact Us</a>
  <h4 style="left:864px">Legal</h4>
  <a style="left:864px;top:3742px">Term Of Services</a>
  <a style="left:864px;top:3776px">Privacy Policy</a>
  <a style="left:864px;top:3810px">Licensed &amp; Regulation</a>
  <h4 style="left:1048px">Socials</h4>
  <a style="left:1048px;top:3742px">Linkedin</a>
  <a style="left:1048px;top:3776px">X</a>
  <a style="left:1048px;top:3810px">Facebook</a>
  <a style="left:1048px;top:3844px">Instagram</a>
</div>
<div class="foot-rule"></div>
<div class="copy">© 2024 TLH All Rights Reserved.</div>

</body>
</html>
```